Redesign my business cards

I would like pretty much all the same information as my current business cards but redesigned to stand out more and be more unique photo uploaded to show my current business cards don’t mind if you want to remove or replace I for on the back

```html
<!DOCTYPE html>
<html lang="en">
<head>
<meta charset="utf-8">
<title>Harbourline Detailing – Business Card</title>
<link rel="stylesheet" href="https://fonts.googleapis.com/css2?family=Aldrich&family=Roboto:wght@400;700&display=swap">
<style>
  :root {
    --page-bg: #2a2a2b;
    --card-top: #0f2d3d;
    --card-bottom: #0a1c28;
    --accent-teal: #4ea9c4;
    --price-blue: #1ea6dd;
    --text-light: #dfe7ec;
    --text-soft: #c9d5dc;
    --rule: #3d9fc2;
    --mark: #3e87b8;
  }
  * { margin: 0; padding: 0; box-sizing: border-box; }
  html, body { width: 1200px; height: 1138px; overflow: hidden; background: var(--page-bg); }
  body { position: relative; font-family: "Roboto", sans-serif; color: var(--text-light); }

  .card {
    position: absolute;
    border-radius: 16px;
    background: linear-gradient(160deg, var(--card-top) 0%, var(--card-bottom) 100%);
    box-shadow: 0 6px 14px rgba(0,0,0,0.45);
    overflow: hidden;
  }
  .card--front { left: 274px; top: 186px; width: 623px; height: 376px; }
  .card--back  { left: 276px; top: 608px; width: 618px; height: 374px; }

  .brand-mark {
    position: absolute;
    display: flex; flex-direction: column; align-items: center; justify-content: center;
    gap: 10px;
    font-family: "Aldrich", sans-serif;
    color: var(--mark);
    text-align: center;
  }
  .brand-mark__dot { border-radius: 50%; background: var(--mark); opacity: 0.55; }
  .card--front .brand-mark { left: 212px; top: 40px; width: 200px; height: 200px; font-size: 22px; line-height: 1.15; letter-spacing: 2px; }
  .card--front .brand-mark__dot { width: 70px; height: 70px; }

  .contact { position: absolute; left: 0; right: 0; text-align: center; }
  .contact__name-line { top: 262px; display: flex; justify-content: center; align-items: baseline; gap: 10px; }
  .contact__name { font-family: "Aldrich", sans-serif; font-size: 26px; color: var(--accent-teal); letter-spacing: 0.5px; }
  .contact__role { font-size: 19px; color: var(--text-soft); }
  .contact__phone { top: 298px; display: flex; justify-content: center; align-items: center; gap: 8px;
    font-size: 23px; font-weight: 700; color: var(--accent-teal); letter-spacing: 0.5px; }
  .contact__email { top: 328px; display: flex; justify-content: center; align-items: center; gap: 12px;
    font-size: 17px; color: var(--text-soft); }

  .service { position: absolute; left: 22px; }
  .service__title { font-family: "Aldrich", sans-serif; font-weight: 400; font-size: 22px; color: var(--text-light); letter-spacing: 0.3px; white-space: nowrap; }
  .service__price { font-family: "Roboto", sans-serif; font-weight: 700; font-size: 28px; color: var(--price-blue); margin-left: 10px; }
  .service__desc { font-size: 14.5px; line-height: 19px; color: var(--text-soft); margin-top: 6px; }
  .service--interior { top: 38px; width: 580px; }
  .service--exterior { top: 133px; width: 580px; }
  .service--full { top: 224px; width: 402px; }
  .service--full .service__desc { text-align: justify; }

  .rule { position: absolute; left: 22px; height: 1.5px; background: var(--rule); }
  .rule--one { top: 121px; width: 577px; }
  .rule--two { top: 216px; width: 428px; }

  .card--back .brand-mark { left: 440px; top: 206px; width: 160px; height: 140px; font-size: 15px; line-height: 1.25; letter-spacing: 1px; gap: 8px; }
  .card--back .brand-mark__dot { width: 56px; height: 56px; }
</style>
</head>
<body>
  <section class="card card--front">
    <div class="brand-mark">
      <span class="brand-mark__dot"></span>
      <span class="brand-mark__name">HARBOURLINE<br>DETAILING</span>
    </div>
    <div class="contact contact__name-line">
      <span class="contact__name">DEAN MARLOWE</span>
      <span class="contact__role">Owner/Operator</span>
    </div>
    <div class="contact contact__phone">
      <svg width="24" height="24" viewBox="0 0 24 24" aria-hidden="true">
        <circle cx="12" cy="12" r="11" fill="none" stroke="#4ea9c4" stroke-width="1.5"/>
        <path d="M8.5 6.5c.6-.4 1.2-.3 1.5.2l1 1.8c.3.5.2 1-.2 1.3l-.8.6c.5 1.3 1.5 2.5 2.8 3.2l.7-.7c.4-.4.9-.4 1.3-.1l1.7 1.1c.5.3.6 1 .2 1.5-.8 1-2 1.4-3.2.9-2.8-1.2-4.9-3.6-5.9-6.4-.4-1.3 0-2.6.9-3.4z" fill="none" stroke="#4ea9c4" stroke-width="1.3"/>
      </svg>
      <span>0412555017</span>
    </div>
    <div class="contact contact__email">
      <svg width="18" height="13" viewBox="0 0 18 13" aria-hidden="true">
        <rect x="0.5" y="0.5" width="17" height="12" fill="#4ea9c4"/>
        <path d="M0.5 0.5 9 7.5 17.5 0.5" fill="none" stroke="#0f2d3d" stroke-width="1.2"/>
      </svg>
      <span>harbourlinedetailing@example.com</span>
    </div>
  </section>

  <section class="card card--back">
    <div class="service service--interior">
      <h2 class="service__title">INTERIOR DETAIL<span class="service__price">$150</span></h2>
      <p class="service__desc">Vacume &amp; Deep clean of carpets &amp; upholstery or leather treatment, interior trim clean &amp; condition, window polish and treatment, steam clean &amp; stain removal</p>
    </div>
    <div class="rule rule--one"></div>
    <div class="service service--exterior">
      <h2 class="service__title">EXTERIOR DETAIL<span class="service__price">$250</span></h2>
      <p class="service__desc">Extreme wash &amp; polish, exterior trim reviver &amp; protector window polish &amp; treatment, tyre dressing, engine bay cleaned</p>
    </div>
    <div class="rule rule--two"></div>
    <div class="service service--full">
      <h2 class="service__title">FULL EXTREME DETAILS<span class="service__price">$350</span></h2>
      <p class="service__desc">Extreme wash and polish, tyre dressing, engine bay cleaned, vacume &amp; deep clean of carpets &amp; upholstery or leather treatment, interior &amp; exterior trim reviver &amp; protector, window polish and treatment</p>
    </div>
    <div class="brand-mark">
      <span class="brand-mark__dot"></span>
      <span class="brand-mark__name">HARBOURLINE<br>DETAILING</span>
    </div>
  </section>
</body>
</html>
```